32 x 24 Swinging Real Estate Yard Sign

We are looking to design a new sign for our business to focus on the remodeling of homes to sell. We are looking to have a yard sign that gets peoples attention and is informational. The headline will be "The Secret to Top Dollar? Remodel First.". We remodel homes for sellers with no up front cost, as they simply pay at closing. This link has more info, https://brightkeelhomes.com/Remodel
The message we want to convey to those seeing the sign is we are a one stop shop, who can renovate your home and sell it for no stress. We are licensed real estate agents and licensed contractors.
Both of these license numbers and info need to be on the design:
CADRE #02741968
Contractors License #2758314
Email: info@brightkeelhomes.com
Phone: (408)514-7290
I'll attach a sample sign we have for our agents normally as well as all brand art work.
• Pantone Colors
o #172A41
Dark blue
o #4381B1
Medium blue
o #6FA6CC
Light blue
Target Market(s)
Residential Real Estate Sellers
Industry/Entity Type
Real Estate
Colors
Designer to choose colors to be used in the design.

```html
<!DOCTYPE html>
<html lang="en">
<head>
<meta charset="utf-8">
<title>Brightkeel Homes – Yard Sign</title>
<link rel="stylesheet" href="https://fonts.googleapis.com/css2?family=Montserrat:wght@500;600;700&family=Oswald:wght@600&display=swap">
<style>
  :root {
    --navy: #172A41;
    --navy-soft: #1D3350;
    --blue: #4381B1;
    --light-blue: #6FA6CC;
    --white: #FFFFFF;
    --backdrop: #E9ECEF;
  }
  * { margin: 0; padding: 0; box-sizing: border-box; }
  html, body {
    width: 1200px;
    height: 1200px;
    overflow: hidden;
    background: var(--backdrop);
    font-family: "Montserrat", sans-serif;
  }
  .yard-sign {
    position: absolute;
    left: 195px;
    top: 42px;
    width: 810px;
    height: 1116px;
    background: var(--white);
    overflow: hidden;
  }
  .sign-shapes {
    position: absolute;
    inset: 0;
    width: 100%;
    height: 100%;
  }
  .shape-navy { fill: var(--navy); }
  .shape-soft { fill: var(--navy-soft); }

  .brand-wordmark {
    position: absolute;
    left: 40px;
    width: 740px;
    top: 250px;
    text-align: center;
    color: var(--navy);
    font-weight: 600;
  }
  .brand-name {
    display: block;
    font-size: 84px;
    line-height: 1;
    letter-spacing: 1px;
  }
  .brand-sub {
    display: block;
    margin-top: 26px;
    font-size: 28px;
    letter-spacing: 0.55em;
    padding-left: 0.55em;
    color: var(--blue);
  }

  .contact-box {
    position: absolute;
    left: 67px;
    top: 590px;
    width: 676px;
    height: 259px;
    border: 3px solid var(--white);
    border-radius: 20px;
  }
  .agent-name {
    position: absolute;
    left: 40px;
    width: 730px;
    top: 534px;
    text-align: center;
    font-family: "Oswald", sans-serif;
    font-weight: 600;
    font-size: 104px;
    line-height: 1.1;
    letter-spacing: -1px;
    color: var(--white);
  }
  .agent-name span {
    background: var(--navy);
    padding: 0 12px;
  }
  .agent-phone {
    position: absolute;
    left: 67px;
    width: 676px;
    top: 672px;
    text-align: center;
    font-weight: 700;
    font-size: 80px;
    line-height: 1.1;
    letter-spacing: -1px;
    color: var(--blue);
  }
  .agent-email {
    position: absolute;
    left: 67px;
    width: 676px;
    top: 780px;
    text-align: center;
    font-weight: 500;
    font-size: 38px;
    line-height: 1.1;
    color: var(--white);
  }

  .remodel-pitch {
    position: absolute;
    left: 71px;
    top: 880px;
    width: 480px;
    color: var(--white);
  }
  .pitch-headline {
    font-weight: 700;
    font-size: 30px;
    line-height: 1.15;
  }
  .pitch-headline .accent { color: var(--light-blue); }
  .pitch-message {
    margin-top: 8px;
    font-weight: 500;
    font-size: 16px;
    line-height: 1.35;
    color: var(--light-blue);
  }

  .website {
    position: absolute;
    left: 71px;
    top: 1036px;
    font-weight: 500;
    font-size: 31px;
    color: var(--white);
  }
  .licenses {
    position: absolute;
    left: 582px;
    top: 950px;
    font-weight: 500;
    font-size: 16px;
    line-height: 1.4;
    text-transform: uppercase;
    color: var(--blue);
  }
  .licenses .license + .license { margin-top: 20px; }
</style>
</head>
<body>
  <main class="yard-sign">
    <svg class="sign-shapes" viewBox="0 0 1030 1420" preserveAspectRatio="none" aria-hidden="true">
      <rect class="shape-navy" x="0" y="578" width="1030" height="842"/>
      <path class="shape-soft" d="M1030 600 C900 800 700 870 520 860 C720 900 920 840 1030 700 Z"/>
      <path class="shape-navy" d="M725 15 L920 15 C1000 180 1010 400 918 578 L898 578 C950 380 880 170 725 15 Z"/>
      <path class="shape-navy" d="M1030 420 C985 470 955 520 940 578 L1030 578 Z"/>
    </svg>

    <div class="brand-wordmark">
      <span class="brand-name">BRIGHTKEEL</span>
      <span class="brand-sub">HOMES</span>
    </div>

    <div class="contact-box"></div>
    <h1 class="agent-name"><span>DANIEL HARTLEY</span></h1>
    <p class="agent-phone">(408)514-7290</p>
    <p class="agent-email">info@brightkeelhomes.com</p>

    <section class="remodel-pitch">
      <h2 class="pitch-headline">The Secret to Top Dollar?<br><span class="accent">Remodel First.</span></h2>
      <p class="pitch-message">We renovate &amp; sell your home. No upfront cost – pay at closing.</p>
    </section>

    <p class="website">brightkeelhomes.com/Remodel</p>
    <div class="licenses">
      <p class="license">CADRE #02741968</p>
      <p class="license">Contractors<br>License #2758314</p>
    </div>
  </main>
</body>
</html>
```